Brightmere Facebook Design

Build out a really nice and professional Facebook Page and full banner for Brightmere perhaps with the our services portfolio across the page as well,
Pls check www.brightmere-example.com.au for ideas to a make the Facebook Page look professional like a similar theme to our website and the porfolio of services

Main photo please emphasis the equipment cleaning and the gurney cleaning a lower priority to emphasize is the general cleaning
Thanks very much

Target Market(s)

Restaurant, warehouses, factories, car and fleet companies, hotels and buffets, chain restaurants, pizza huts, burger eateries, leisure centres

Industry/Entity Type

Cleaning Services

Font styles to use
Serif

Colors
3277b5
f04a50
f37122
fcf299
ec1f27

Requirements
Must have
• Energy and professional Facebook Site with some of the Brightmere Flowers across it and the portfolio of services
Nice to have
• Good vibrant colours

Professional similar to the website

```html
<!DOCTYPE html>
<html lang="en">
<head>
<meta charset="utf-8">
<title>Brightmere Facebook Banner Concepts</title>
<link rel="stylesheet" href="https://fonts.googleapis.com/css2?family=Philosopher:wght@400;700&family=Roboto+Condensed:wght@500&display=swap">
<style>
  :root {
    --stage: #2f2f2f;
    --navy: #1d3a6e;
    --navy-dark: #14305e;
    --red: #d9362c;
    --orange: #f0561e;
    --white: #ffffff;
    --paper: #f4f8fc;
    --ink: #1f2f55;
    --contact: #2b2b3a;
    --icon: #f06b5b;
  }
  * { margin: 0; padding: 0; box-sizing: border-box; }
  html, body { width: 1200px; height: 966px; overflow: hidden; }
  body {
    background: radial-gradient(ellipse at 50% 45%, #3a3a3a 0%, var(--stage) 70%, #262626 100%);
    font-family: "Philosopher", sans-serif;
    position: relative;
  }
  .concept-label {
    position: absolute;
    left: 106px;
    font-family: "Roboto Condensed", sans-serif;
    font-weight: 500;
    font-size: 21px;
    color: var(--white);
  }
  .concept-label--one { top: 38px; }
  .concept-label--two { top: 472px; }

  .banner {
    position: absolute;
    left: 108px;
    width: 984px;
    height: 373px;
    overflow: hidden;
    background: var(--paper);
    box-shadow: 0 6px 24px rgba(0,0,0,.45);
  }
  .banner--one { top: 72px; }
  .banner--two { top: 505px; }
  .banner svg.shapes { position: absolute; inset: 0; width: 984px; height: 373px; }

  /* concept one */
  .brand-mark {
    position: absolute;
    left: 290px; top: 70px;
    width: 120px;
    text-align: center;
    color: var(--white);
    font-weight: 700;
    font-size: 20px;
    line-height: 26px;
  }
  .headline {
    position: absolute;
    left: 482px; top: 36px;
    color: var(--red);
    font-weight: 700;
    font-size: 41px;
    line-height: 43px;
  }
  .contact-list {
    position: absolute;
    left: 486px; top: 244px;
    list-style: none;
    color: var(--contact);
    font-size: 17px;
  }
  .contact-list li { display: flex; align-items: center; height: 32px; white-space: nowrap; }
  .contact-list svg { width: 18px; height: 18px; margin-right: 10px; flex: none; }
  .service-list {
    position: absolute;
    left: 773px; top: 46px;
    list-style: none;
    color: var(--ink);
    font-size: 17.5px;
    line-height: 24px;
  }
  .service-list li { margin-bottom: 13px; }
  .service-list .num { color: var(--red); }

  /* concept two */
  .logo-lockup {
    position: absolute;
    left: 36px; top: 204px;
    display: flex; align-items: center;
    color: var(--orange);
    font-size: 29px;
  }
  .logo-lockup .dot {
    width: 22px; height: 22px; border-radius: 50%;
    background: var(--navy); margin-right: 10px;
  }
  .hero-title {
    position: absolute;
    left: 348px; top: 94px;
    width: 221px;
    text-align: center;
    color: var(--white);
    font-weight: 700;
    font-size: 27px;
    line-height: 36px;
  }
  .check-item {
    position: absolute;
    display: flex; align-items: center;
    color: var(--white);
    font-size: 17px;
    line-height: 24px;
  }
  .check-item svg { width: 30px; height: 30px; margin-right: 12px; flex: none; }
</style>
</head>
<body>

<div class="concept-label concept-label--one">Concept Version 1</div>
<section class="banner banner--one">
  <svg class="shapes" viewBox="0 0 820 311" preserveAspectRatio="none">
    <defs>
      <linearGradient id="teamPhoto" x1="0" y1="0" x2="1" y2="1">
        <stop offset="0" stop-color="#c9d3dc"/>
        <stop offset=".5" stop-color="#7fb3d8"/>
        <stop offset="1" stop-color="#4a6f96"/>
      </linearGradient>
    </defs>
    <rect x="0" y="0" width="380" height="311" fill="url(#teamPhoto)" role="img" aria-label="Photo of smiling cleaning staff in blue uniforms with a cleaning trolley"/>
    <path d="M390,0 C330,60 350,180 370,311 L820,311 L820,0 Z" fill="var(--paper)"/>
    <path d="M215,0 C195,80 310,130 352,311 L370,311 C350,180 330,60 390,0 Z" fill="var(--navy-dark)" stroke="var(--white)" stroke-width="7"/>
  </svg>
  <div class="brand-mark">Brightmere</div>
  <h1 class="headline">Commercial<br>Cleaning &amp;<br>Maintenance</h1>
  <ul class="contact-list">
    <li><svg viewBox="0 0 24 24"><path fill="var(--icon)" d="M6.6 10.8a15 15 0 0 0 6.6 6.6l2.2-2.2c.3-.3.7-.4 1-.2 1.1.4 2.3.6 3.6.6.6 0 1 .4 1 1V20c0 .6-.4 1-1 1A17 17 0 0 1 3 4c0-.6.4-1 1-1h3.5c.6 0 1 .4 1 1 0 1.3.2 2.5.6 3.6.1.3 0 .7-.2 1z"/></svg>0400 318 562</li>
    <li><svg viewBox="0 0 24 24"><rect x="2" y="5" width="20" height="14" rx="1.5" fill="var(--icon)"/><path d="M3 6l9 7 9-7" stroke="#fff" stroke-width="1.6" fill="none"/></svg>mail@brightmere-example.au</li>
    <li><svg viewBox="0 0 24 24"><path fill="var(--icon)" d="M12 2a7 7 0 0 0-7 7c0 5 7 13 7 13s7-8 7-13a7 7 0 0 0-7-7zm0 9.5A2.5 2.5 0 1 1 12 6.5a2.5 2.5 0 0 1 0 5z"/></svg>Lakeview, QLD, 4100</li>
  </ul>
  <ol class="service-list">
    <li><span class="num">1.</span> Equipment Cleaning<br>&amp; Sanitisation</li>
    <li><span class="num">2.</span> Kitchen<br>Detail Cleaning</li>
    <li><span class="num">3.</span> General Cleaning &amp;<br>Property Facilities</li>
    <li><span class="num">4.</span> High pressure gurney<br>&amp; play ground equipment</li>
    <li><span class="num">5.</span> Projects and<br>Recruiting Services</li>
  </ol>
</section>

<div class="concept-label concept-label--two">Concept Version 2</div>
<section class="banner banner--two">
  <svg class="shapes" viewBox="0 0 820 311" preserveAspectRatio="none">
    <defs>
      <linearGradient id="workerPhoto" x1="0" y1="0" x2="1" y2="0">
        <stop offset="0" stop-color="#9fb4c8"/>
        <stop offset=".4" stop-color="#c8d9e6"/>
        <stop offset="1" stop-color="#eef2f6"/>
      </linearGradient>
    </defs>
    <rect x="0" y="0" width="820" height="311" fill="url(#workerPhoto)" role="img" aria-label="Photo of a cleaner in a blue uniform wiping a surface with yellow gloves"/>
    <path d="M620,0 C565,150 520,230 475,311 L670,311 C740,250 795,190 820,140 L820,0 Z" fill="var(--navy)"/>
    <circle cx="140" cy="340" r="212" fill="var(--paper)"/>
    <circle cx="382" cy="124" r="99" fill="var(--white)"/>
    <circle cx="382" cy="124" r="91" fill="var(--navy)"/>
  </svg>
  <div class="logo-lockup"><span class="dot"></span>Brightmere</div>
  <h2 class="hero-title">Commercial Cleaning and Maintenance</h2>
  <div class="check-item" style="left:723px;top:18px"><svg viewBox="0 0 30 30"><circle cx="15" cy="15" r="14" fill="var(--orange)"/><path d="M8.5 15.5l4.5 4.5 8.5-9" stroke="#fff" stroke-width="2.8" fill="none" stroke-linecap="round" stroke-linejoin="round"/></svg>Equipment Cleaning<br>&amp; Sanitisation</div>
  <div class="check-item" style="left:711px;top:95px"><svg viewBox="0 0 30 30"><circle cx="15" cy="15" r="14" fill="var(--orange)"/><path d="M8.5 15.5l4.5 4.5 8.5-9" stroke="#fff" stroke-width="2.8" fill="none" stroke-linecap="round" stroke-linejoin="round"/></svg>Kitchen Detail Cleaning</div>
  <div class="check-item" style="left:690px;top:147px"><svg viewBox="0 0 30 30"><circle cx="15" cy="15" r="14" fill="var(--orange)"/><path d="M8.5 15.5l4.5 4.5 8.5-9" stroke="#fff" stroke-width="2.8" fill="none" stroke-linecap="round" stroke-linejoin="round"/></svg>General Cleaning &amp;<br>Property Facilities</div>
  <div class="check-item" style="left:654px;top:216px"><svg viewBox="0 0 30 30"><circle cx="15" cy="15" r="14" fill="var(--orange)"/><path d="M8.5 15.5l4.5 4.5 8.5-9" stroke="#fff" stroke-width="2.8" fill="none" stroke-linecap="round" stroke-linejoin="round"/></svg>High pressure gurney<br>&amp; play ground equipment</div>
  <div class="check-item" style="left:597px;top:294px"><svg viewBox="0 0 30 30"><circle cx="15" cy="15" r="14" fill="var(--orange)"/><path d="M8.5 15.5l4.5 4.5 8.5-9" stroke="#fff" stroke-width="2.8" fill="none" stroke-linecap="round" stroke-linejoin="round"/></svg>Projects and<br>Recruiting Services</div>
</section>

</body>
</html>
```